Kestrel Dental personal information forms

We are a Dental Practice that require an update to our information forms, there are 3 versions of it.
I will attach our old ones, we need to keep the same information on there, we just want them to look better and use our current logo and colours.
Our website is www.kestreldental.net
Our facebook is www.friendnook.com/kestreldentalbrookplaza/
..................................................................................................

Target Market(s)

Everyone, easy to read

Industry/Entity Type

Dental Clinic

Colors
0692cd
34a6d7
cee9f5
ffffff
0255a3
3276b5

Requirements
Must have
• Logo
• Our colours
• same information as the uploaded versions
Should not have
• any other colour besides the blues, black and white

```html
<!DOCTYPE html>
<html lang="en">
<head>
<meta charset="utf-8">
<title>Kestrel Dental – Medical History Update</title>
<link rel="stylesheet" href="https://fonts.googleapis.com/css2?family=Oswald:wght@500&family=Roboto+Slab:wght@700&family=Roboto:wght@400&family=Roboto+Condensed:wght@400&display=swap">
<style>
  :root {
    --blue-deep: #0255a3;
    --blue-mid: #3276b5;
    --blue-main: #34a6d7;
    --blue-bright: #0692cd;
    --blue-pale: #cee9f5;
    --ink: #1a1a1a;
    --white: #ffffff;
    --field-top: #f2f2f2;
    --field-bottom: #c9c9c9;
  }
  * { margin: 0; padding: 0; box-sizing: border-box; }
  html, body { width: 974px; height: 1200px; overflow: hidden; background: var(--white); }
  .sheet { position: relative; width: 974px; height: 1200px; background: var(--white); color: var(--ink); font-family: "Roboto Condensed", sans-serif; }

  .header-top { position: absolute; left: 0; top: 0; width: 974px; height: 21px; background: #47ace0; }
  .header-band { position: absolute; left: 0; top: 21px; width: 974px; height: 125px; background: var(--blue-main); }
  .header-block { position: absolute; left: 0; top: 0; width: 280px; height: 146px; background: var(--blue-deep); }
  .header-rule { position: absolute; left: 0; top: 146px; width: 974px; height: 20px; background: var(--blue-pale); }

  .brand { position: absolute; left: 0; top: 44px; width: 280px; text-align: center; font-family: "Roboto", sans-serif; font-size: 34px; color: var(--white); }

  .practitioners { position: absolute; left: 280px; right: 0; top: 34px; text-align: center; font-family: "Oswald", sans-serif; font-weight: 500; color: var(--white); line-height: 1; }
  .practitioners .names { font-size: 36px; }
  .practitioners .role { font-size: 32px; margin-top: 12px; }

  .welcome { position: absolute; left: 380px; width: 520px; top: 184px; text-align: center; font-family: "Roboto Slab", serif; font-weight: 700; font-size: 36px; line-height: 43px; color: var(--blue-deep); }

  .intro { position: absolute; left: 23px; width: 928px; top: 304px; font-family: "Roboto", sans-serif; font-size: 17.5px; line-height: 21px; text-align: justify; }

  .question { position: absolute; left: 23px; width: 928px; font-size: 17px; display: flex; justify-content: space-between; }
  .yes-no { font-weight: 400; color: var(--blue-deep); font-family: "Oswald", sans-serif; font-size: 17px; }
  .field { position: absolute; left: 23px; width: 928px; height: 33px; border-radius: 17px; border: 1px solid #bdbdbd; background: linear-gradient(var(--field-top), var(--field-bottom)); }

  .conditions { position: absolute; left: 54px; top: 548px; width: 900px; }
  .column { position: absolute; top: 0; list-style: none; }
  .column li { height: 23px; font-size: 17px; line-height: 22px; display: flex; align-items: center; gap: 10px; }
  .tickbox { width: 12px; height: 12px; border: 1px solid #aaa; background: linear-gradient(#fafafa, #d6d6d6); }

  .declaration { position: absolute; left: 23px; width: 928px; top: 1043px; font-size: 16.5px; line-height: 20px; }
  .signature { position: absolute; left: 23px; width: 928px; top: 1092px; font-size: 16.5px; display: flex; }
  .sign-line { border-bottom: 1.5px dashed #333; height: 16px; }

  .footer { position: absolute; left: 0; top: 1128px; width: 974px; height: 72px; }
</style>
</head>
<body>
<div class="sheet">
  <div class="header-top"></div>
  <div class="header-band"></div>
  <div class="header-block"></div>
  <div class="header-rule"></div>
  <div class="brand">Kestrel Dental</div>

  <div class="practitioners">
    <div class="names">Dr. Peter Halvorsen &amp; Dr. Simon Ashby</div>
    <div class="role">DENTAL SURGEONS</div>
  </div>

  <h1 class="welcome">Welcome back to<br>our practice</h1>

  <p class="intro">THIS INFORMATION IS CONFIDENTIAL and isnecessary to enable us to offer you THE BEST POSSIBLE CARE. It is now mandatory to have a written updated medical history every 2 years and we would appreciate your time in thoroughly completing this form.</p>

  <div class="question" style="top:373px"><span>Are you currently or have you taken any prescribed medication or dietary supplements in the last 12 months?</span><span class="yes-no">YES / NO</span></div>
  <div class="field" style="top:404px"></div>

  <div class="question" style="top:447px"><span>Allergies / Reactions ? If YES, please list below</span><span class="yes-no">YES / NO</span></div>
  <div class="field" style="top:475px"></div>

  <div class="question" style="top:518px"><span>Have you ever had or are you suffering from any of the following? Please tick any that apply:</span></div>

  <div class="conditions">
    <ul class="column" style="left:0">
      <li><span class="tickbox"></span>Rheumatic fever</li>
      <li><span class="tickbox"></span>Epilepsy</li>
      <li><span class="tickbox"></span>Asthma</li>
      <li><span class="tickbox"></span>Tubersulosis</li>
      <li><span class="tickbox"></span>Radiation Therapy</li>
      <li><span class="tickbox"></span>Dizziness, Fainting</li>
      <li><span class="tickbox"></span>Hepatitis A B or C</li>
      <li><span class="tickbox"></span>Recent Eye Surgery</li>
    </ul>
    <ul class="column" style="left:364px">
      <li><span class="tickbox"></span>Diabetes</li>
      <li><span class="tickbox"></span>Kidney Disease</li>
      <li><span class="tickbox"></span>Heart Attack</li>
      <li><span class="tickbox"></span>High Blood Pressure</li>
      <li><span class="tickbox"></span>Bleeding problems</li>
      <li><span class="tickbox"></span>Artificial joints</li>
      <li><span class="tickbox"></span>Respiratory problems</li>
    </ul>
    <ul class="column" style="left:720px">
      <li><span class="tickbox"></span>HIV Positive</li>
      <li><span class="tickbox"></span>High cholesterol</li>
      <li><span class="tickbox"></span>Cancer</li>
      <li><span class="tickbox"></span>Pace-maker</li>
      <li><span class="tickbox"></span>Osteoporosis</li>
      <li><span class="tickbox"></span>Heart rate problems</li>
      <li><span class="tickbox"></span>Heart murmur</li>
    </ul>
  </div>

  <div class="question" style="top:745px"><span>Do you have any disease, condition or problem not listed above?</span><span class="yes-no">YES / NO</span></div>
  <div class="field" style="top:774px"></div>

  <div class="question" style="top:822px"><span>Have you had surgery or been to hospital in the last 5 years? (if YES, please give details)</span><span class="yes-no">YES / NO</span></div>
  <div class="field" style="top:853px"></div>

  <div class="question" style="top:896px"><span>For Women : Are you pregnant? If yes, how many months?</span><span class="yes-no">YES / NO</span></div>
  <div class="field" style="top:925px"></div>

  <div class="question" style="top:970px"><span>Do you currently or have you ever smoked?</span><span class="yes-no">YES / NO</span></div>
  <div class="field" style="top:1001px"></div>

  <p class="declaration">The information that I have provided is to the best of my knowledge true and correct and I understand that it is my responsiibility to inform of any change in my medical status.</p>

  <div class="signature">
    <span>Patient / Parent / Person Responsible Signature :</span>
    <span class="sign-line" style="width:228px;margin-left:16px"></span>
    <span style="margin-left:56px">Date:</span>
    <span class="sign-line" style="width:220px;margin-left:16px"></span>
  </div>

  <svg class="footer" width="974" height="72" viewBox="0 0 974 72" aria-hidden="true">
    <rect x="0" y="10" width="974" height="62" fill="var(--blue-main)"/>
    <rect x="0" y="0" width="800" height="11" fill="var(--blue-deep)"/>
    <polygon points="800,0 886,42 974,0 974,11 886,55 800,11" fill="var(--blue-deep)"/>
    <polygon points="800,0 974,0 886,42" fill="var(--white)"/>
  </svg>
</div>
</body>
</html>
```